Broschüren-Design für gemeinnützige Organisation
Zielgruppe
Als gemeinnützige Organisation unterstützen wir Kinder und Jugendliche, vor allem in den Bereichen Schul- und Berufsausbildung. Wir arbeiten vorwiegend in Ostafrika, vor allem in Tansania und Kenia. Mit dieser Broschüre wollen wir für unser neues Pilotprojekt werben, den Aufbau eines dualen Ausbildungszentrums für junge Menschen in Kenia. Ziel des Ausbildungszentrums ist es jungen Menschen eine qualifizierte Berufsausbildung zu ermöglichen und damit Perspektiven und Zukunft im Heimatland.
Unsere Zielgruppe: Menschen mit Herz und Weitblick von 18 bis 80+
Aufgabenstellung
Die Broschüre sollte handlich sein und leicht zum einstecken. Derzeit haben wir den Text und die Gestaltung auf das Format DIN lang hoch (105x210 mm, 12 Seiten) ausgelegt. Ist aber nur ein Vorschlag und kein muss.
Die einzige Vorgabe ist das orange aus dem Logo mit der Farbe #ff3300 Ansonsten gibt es keine Vorgaben was Schrift, Farbgestaltung, Layout, Form, Seitenanzahl...ect betrifft. Allerdings sollte darauf geachtet werden, dass die Textinhalte der Doppelseiten erhalten bleiben (z.B. Seite 2 links - Seite 3 rechts, usw.)
Mitgeliefert werden Fotos, die gerne Verwendung finden können. Sollten aber weitere oder aussagekräftigere Fotos und Hintergründe benötigt werden, sind wir absolut offen dafür.

```html
<!DOCTYPE html>
<html lang="de">
<head>
<meta charset="utf-8">
<title>Heimat als Chance – Broschüre</title>
<link href="https://fonts.googleapis.com/css2?family=Oswald:wght@500;700&family=Cabin:ital,wght@0,400;0,700;1,400;1,700&display=swap" rel="stylesheet">
<style>
:root{
  --orange:#e4571d;
  --purple:#2e2c8c;
  --ink:#232323;
  --paper:#f5f5f4;
  --cover:#e3e2df;
  --label:#efeeec;
  --backdrop:#d9d9de;
}
*{box-sizing:border-box;margin:0;padding:0}
html,body{width:822px;height:1200px;overflow:hidden}
body{background:var(--backdrop);font-family:"Cabin",sans-serif;color:var(--ink);position:relative}
.spread{position:absolute;left:31px;width:760px;height:540px;display:flex;box-shadow:0 8px 24px rgba(0,0,0,.18)}
.spread--cover{top:30px}
.spread--inner{top:630px}
.page{position:relative;width:380px;height:540px;overflow:hidden}
.spread--cover .page{background:var(--cover)}
.spread--inner .page{background:var(--paper);display:flex;flex-direction:column;padding:20px 30px 18px}
.spread--inner .page--left{border-right:1px solid #dedede}

.photo{position:absolute;border-radius:50%}
.photo--girls{left:20px;top:-120px;width:370px;height:370px;background:radial-gradient(circle at 50% 65%,#8a5a3a,#4d3324 60%,#2e241e)}
.photo--boy{left:95px;top:50px;width:340px;height:340px;background:radial-gradient(circle at 55% 40%,#9a958d,#5a5650 55%,#3a3835)}

.headline{font-family:"Oswald",sans-serif;font-weight:700;text-transform:uppercase;line-height:.95;letter-spacing:1px}
.label{position:absolute;background:var(--label);padding:6px 12px;border-radius:4px}
.thanks{left:80px;top:228px;font-size:50px}
.thanks .accent,.title .accent{color:var(--orange)}
.title{left:20px;top:300px;font-size:46px;background:#f4f4f2;z-index:2}

.brand{display:flex;align-items:center;gap:6px;font-family:"Cabin",sans-serif;font-weight:700;font-size:11px;line-height:1.1;color:var(--ink);text-transform:uppercase}
.brand__dot{width:14px;height:14px;border-radius:50%;background:var(--orange);flex:none}
.brand--back{position:absolute;left:170px;top:370px}
.logo-box{position:absolute;left:40px;top:22px;width:150px;height:70px;background:#fafaf9;display:flex;align-items:center;justify-content:center;z-index:3;box-shadow:0 1px 3px rgba(0,0,0,.12)}

.contact{position:absolute;left:170px;top:410px;font-size:11px;line-height:1.35}
.contact strong{font-weight:700}
.contact .gap{margin-top:6px}

.tag{position:absolute;left:20px;top:418px;width:228px;background:var(--orange);color:#fff;font-size:12px;line-height:1.3;padding:7px 12px;border-radius:4px;z-index:2}

.h2{font-family:"Oswald",sans-serif;font-weight:700;text-transform:uppercase;font-size:22px;line-height:1.2;letter-spacing:1px;color:var(--orange)}
.h2--purple{color:var(--purple)}
.body{font-size:10.5px;line-height:1.38;margin-top:4px}

.quote{display:flex;gap:14px;align-items:center;margin:14px 0 12px}
.quote__photo{width:92px;height:92px;border-radius:50%;flex:none;background:radial-gradient(circle,#8f8b85,#4a4743)}
.quote__box{flex:1;position:relative;padding:12px 0 14px}
.quote__box::before,.quote__box::after{content:"";position:absolute;height:1px;background:var(--orange)}
.quote__box::before{left:18px;right:0;top:5px}
.quote__box::after{left:0;right:18px;bottom:5px}
.quote__mark{position:absolute;font-family:"Oswald",sans-serif;font-weight:700;font-size:20px;color:var(--orange);line-height:1;background:var(--paper)}
.quote__open{left:0;top:-3px}
.quote__close{right:0;bottom:-5px}
.quote__text{font-weight:700;font-style:italic;font-size:11px;line-height:1.4}
.quote__who{font-size:8px;color:#555;margin-top:4px}

.note{margin-top:auto;height:64px;border:1.5px solid var(--orange);display:flex;align-items:center;justify-content:center;text-align:center;padding:0 20px;font-family:"Oswald",sans-serif;font-weight:500;font-size:12px;line-height:1.4}

.team{position:relative;height:160px;flex:none}
.member{position:absolute;width:78px;text-align:center;font-size:10px;line-height:1.2}
.member__photo{width:64px;height:64px;border-radius:50%;margin:0 auto 4px;background:radial-gradient(circle,#d9b8a0,#a98872)}
.member:nth-child(1){left:20px;top:0}
.member:nth-child(2){left:90px;top:56px}
.member:nth-child(3){left:170px;top:10px}
.member:nth-child(4){left:240px;top:66px}
.who{margin-top:4px}
.help{margin-top:10px}
.help ul{list-style:none}
.help li::before{content:"• "}

.pilot{position:relative;margin-top:auto;height:70px;border:1.5px solid var(--purple);text-align:center;padding:12px 16px 0;flex:none}
.pilot__label{position:absolute;left:50%;top:-7px;transform:translateX(-50%);background:var(--paper);padding:0 8px;font-family:"Oswald",sans-serif;font-weight:500;font-size:9px;color:var(--purple);letter-spacing:.5px;white-space:nowrap}
.pilot__title{font-family:"Oswald",sans-serif;font-weight:700;font-size:12px;line-height:1.3}
.pilot__sub{font-family:"Oswald",sans-serif;font-weight:500;font-size:9px;color:var(--purple);margin-top:4px}
</style>
</head>
<body>

<section class="spread spread--cover">
  <div class="page page--back">
    <div class="photo photo--girls" role="img" aria-label="Foto: zwei lächelnde Mädchen mit Kopftüchern und Perlenketten"></div>
    <div class="label headline thanks">Herzlichen<br><span class="accent">Dank</span></div>
    <div class="brand brand--back"><span class="brand__dot"></span><span>Brookwinkel<br>Kinderhilfswerk e.V.</span></div>
    <div class="contact">
      <p>Ahornstraße 24</p>
      <p>80999 München</p>
      <p>089 555 01 234</p>
      <p>info@brookwinkel.de</p>
      <p><strong>www.brookwinkel.de</strong></p>
      <p class="gap"><strong>Spendenkonto</strong></p>
      <p>Sparkasse Nordufer</p>
      <p>IBAN: DE00 1234 5678 0000 0000 00</p>
    </div>
  </div>
  <div class="page page--front">
    <div class="logo-box"><div class="brand"><span class="brand__dot"></span><span>Brookwinkel<br>Kinderhilfswerk e.V.</span></div></div>
    <div class="photo photo--boy" role="img" aria-label="Schwarz-Weiß-Foto: Junge mit Stoffbeutel über der Schulter"></div>
    <div class="label headline title">Heimat als<br><span class="accent">Chance</span></div>
    <div class="tag">Berufsausbildung Benachteiligter Jugendlicher In Ihrer Heimat</div>
  </div>
</section>

<section class="spread spread--inner">
  <div class="page page--left">
    <div class="challenge">
      <h2 class="h2">Die Herausforderung</h2>
      <p class="body">Eine duale Ausbildung gibt es nicht in Afrika. Über 70% der Jugendlichen haben deshalb keinen Zugang zu einer Berufsausbildung und damit keine Chance, dem Teufelsrad aus Elend und Armut zu entkommen.<br>Ohne Perspektiven verlassen sie ihre Heimat, angezogen vom Leitstern Europa, auf der Suche nach einem besseren Leben.</p>
    </div>
    <figure class="quote">
      <div class="quote__photo" role="img" aria-label="Schwarz-Weiß-Foto: Jugendlicher vor einer Hütte"></div>
      <div class="quote__box">
        <span class="quote__mark quote__open">”</span>
        <blockquote class="quote__text">Ich schau mich um in meiner Heimat und weiß, hier wird sich nichts für mich ändern. Nicht heute, nicht morgen. Ich habe nichts zu verlieren, also gehe ich.</blockquote>
        <figcaption class="quote__who">Samuel, 17 J., Tagelöhner</figcaption>
        <span class="quote__mark quote__close">“</span>
      </div>
    </figure>
    <div class="solution">
      <h2 class="h2 h2--purple">Die Lösung</h2>
      <p class="body">Es müssen Zukunftschancen und neue Perspektiven für junge Menschen in ihrer Heimat geschaffen werden. Der Plan? Ein duales Ausbildungszentrum aufbauen, das qualifizierte Ausbildungsplätze anbietet. Es soll hunderten Jugendlichen eine Berufsausbildung in ihrer Heimat ermöglichen und sich am Ende selbst finanzieren können.</p>
    </div>
    <div class="note">Wie Sie helfen können und auch unser „Dankeschön“ an Sie, erfahren Sie auf den nächsten Seiten.</div>
  </div>
  <div class="page page--right">
    <div class="team">
      <div class="member"><div class="member__photo" role="img" aria-label="Porträtfoto Teammitglied"></div>Lena<br>Wirth</div>
      <div class="member"><div class="member__photo" role="img" aria-label="Porträtfoto Teammitglied"></div>Gisela<br>Brandt</div>
      <div class="member"><div class="member__photo" role="img" aria-label="Porträtfoto Teammitglied"></div>Jonas<br>Feller</div>
      <div class="member"><div class="member__photo" role="img" aria-label="Porträtfoto Teammitglied"></div>Katrin<br>Olbers</div>
    </div>
    <div class="who">
      <h2 class="h2">Wer wir sind</h2>
      <p class="body">Als gemeinnütziger Verein unterstützt Brookwinkel Kinderhilfswerk e.V. besonders benachteiligte Kinder und Jugendliche in Ostafrika, vor allem in den Ländern Tansania und Kenia. Seit 2005 sind wir als gemeinnützig anerkannt und eingetragen im Vereinsregister München unter VR 24610.</p>
    </div>
    <div class="help">
      <h2 class="h2">Wie wir helfen</h2>
      <div class="body">
        <p>Im Mittelpunkt unserer Arbeit stehen vor allem</p>
        <ul>
          <li>Schul- und Berufsausbildung benachteiligter Kinder und Jugendlicher</li>
          <li>Nothilfe für Mädchen auf der Flucht vor Beschneidung und Zwangsehe</li>
          <li>Unterstützung von Kinderfamilien, die ohne Eltern auf sich alleine gestellt sind</li>
        </ul>
      </div>
    </div>
    <div class="pilot">
      <span class="pilot__label">UNSER DERZEITIGES PILOTPROJEKT</span>
      <p class="pilot__title">Aufbau und Integration einer dualen Berufsausbildung<br>für Jugendliche in Kenia.</p>
      <p class="pilot__sub">Über dieses Projekt möchten wir Sie in dieser Broschüre informieren.</p>
    </div>
  </div>
</section>

</body>
</html>
```